Makeup artist looking for business card design

- Business card to be memorable and recognisable

- I've attached photos of my logo (File 4), photos that I want to incorporate into the design (File 5,6 & 7) and an example of the design I like "Mirela Stott" (File 1)

- I've attached 3 photos of the designs I want to use, please use one of your choice

- Next to Instagram (File 2) and Facebook (File 3), please use their logo.

- No coloured background, either use the original background (grey) old white.

- Please include the following on the business card:
- Business name: LK Makeup Artistry
- My name: Rosalind Kerr
- Occupation: Makeup Artist
- Contact number: 0437 295 148
- Email: roskerr_makeup@mailvento.com
- Instagram (please use image): @lkmakeupartistry
- Facebook (please use image): www.socialvento.com/LKMakeUpArtistry

Target Market(s)

Target woman for bridal makeup, occasion, fashion makeup and print.

Industry/Entity Type

Business

Requirements
Must have
• Logo provided and photo provided
Should not have
• Colourful background
Too cluttered
Shouldn't use old style font

```html
<!DOCTYPE html>
<html lang="en">
<head>
<meta charset="utf-8">
<title>LK Makeup Artistry – Business Card</title>
<link rel="stylesheet" href="https://fonts.googleapis.com/css2?family=Advent+Pro:wght@200;300;400&family=Raleway:wght@400&display=swap">
<style>
  :root {
    --canvas-bg: #f3f3f4;
    --card-bg: #ecebef;
    --card-shadow: rgba(60, 55, 70, 0.14);
    --ink-dark: #3d3c40;
    --ink-mid: #6f6d73;
    --ink-light: #a4a2a8;
    --icon-grey: #8d8b91;
    --lilac-light: #ede4f0;
    --lilac-mid: #cbb2d6;
    --lilac-deep: #a887b9;
  }
  * { margin: 0; padding: 0; box-sizing: border-box; }
  html, body {
    width: 1200px;
    height: 720px;
    overflow: hidden;
    background: var(--canvas-bg);
  }
  .canvas {
    position: relative;
    width: 1200px;
    height: 720px;
    display: flex;
    align-items: center;
    justify-content: center;
    gap: 50px;
  }
  .card {
    position: relative;
    width: 520px;
    height: 318px;
    background: var(--card-bg);
    box-shadow: 0 6px 18px var(--card-shadow);
    overflow: hidden;
  }

  /* Brand mark (wordmark) */
  .brand {
    position: absolute;
    display: flex;
    align-items: center;
    gap: 10px;
    font-family: "Advent Pro", sans-serif;
    font-weight: 300;
    color: var(--ink-mid);
    text-transform: uppercase;
    white-space: nowrap;
  }
  .brand__dot {
    width: 14px;
    height: 14px;
    border-radius: 50%;
    background: var(--ink-dark);
  }

  /* Front */
  .card--front .brand { left: 48px; top: 44px; font-size: 17px; letter-spacing: 2px; }
  .identity {
    position: absolute;
    left: 48px;
    top: 134px;
    font-family: "Advent Pro", sans-serif;
    font-weight: 300;
    font-size: 24px;
    line-height: 1;
    letter-spacing: 4px;
    text-transform: uppercase;
    white-space: nowrap;
  }
  .identity__name { color: var(--ink-dark); }
  .identity__role { color: var(--ink-light); margin-left: 10px; }

  .contacts {
    position: absolute;
    left: 112px;
    top: 182px;
    list-style: none;
    font-family: "Raleway", sans-serif;
    font-size: 12px;
    color: var(--ink-mid);
  }
  .contacts__item {
    display: flex;
    align-items: center;
    gap: 12px;
    height: 27px;
    white-space: nowrap;
  }
  .contacts__icon {
    width: 18px;
    height: 18px;
    flex: none;
    display: flex;
    align-items: center;
    justify-content: center;
  }
  .contacts__icon--social {
    background: var(--icon-grey);
    border-radius: 3px;
  }

  /* Back */
  .photo {
    position: absolute;
    right: 0;
    top: 0;
    width: 280px;
    height: 100%;
    background:
      radial-gradient(circle at 65% 40%, var(--lilac-light) 0, var(--lilac-mid) 38%, transparent 62%),
      linear-gradient(110deg, #d9d5dc 0%, var(--lilac-mid) 55%, var(--lilac-deep) 100%);
  }
  .card--back .brand { left: 28px; bottom: 46px; font-size: 13px; letter-spacing: 1px; gap: 8px; }
  .card--back .brand__dot { width: 12px; height: 12px; }
</style>
</head>
<body>
<main class="canvas">

  <section class="card card--front" aria-label="Business card front">
    <div class="brand"><span class="brand__dot"></span>LK Makeup Artistry</div>

    <h1 class="identity">
      <span class="identity__name">Rosalind Kerr</span><span class="identity__role">Makeup Artist</span>
    </h1>

    <ul class="contacts">
      <li class="contacts__item">
        <span class="contacts__icon">
          <svg width="16" height="16" viewBox="0 0 24 24" aria-hidden="true">
            <path fill="#3d3c40" d="M6.6 10.8c1.4 2.8 3.8 5.1 6.6 6.6l2.2-2.2c.3-.3.7-.4 1-.2 1.1.4 2.3.6 3.6.6.6 0 1 .4 1 1V20c0 .6-.4 1-1 1C10.6 21 3 13.4 3 4c0-.6.4-1 1-1h3.5c.6 0 1 .4 1 1 0 1.3.2 2.5.6 3.6.1.3 0 .7-.2 1l-2.3 2.2z"/>
          </svg>
        </span>0437 295 148
      </li>
      <li class="contacts__item">
        <span class="contacts__icon">
          <svg width="17" height="17" viewBox="0 0 24 24" aria-hidden="true">
            <circle cx="12" cy="12" r="11" fill="#dcdbe0"/>
            <text x="12" y="16.5" text-anchor="middle" font-family="Raleway, sans-serif" font-size="13" fill="#4f79b5">@</text>
          </svg>
        </span>roskerr_makeup@mailvento.com
      </li>
      <li class="contacts__item">
        <span class="contacts__icon contacts__icon--social" aria-hidden="true"></span>@lkmakeupartistry
      </li>
      <li class="contacts__item">
        <span class="contacts__icon contacts__icon--social" aria-hidden="true"></span>www.socialvento.com/LKMakeUpArtistry
      </li>
    </ul>
  </section>

  <section class="card card--back" aria-label="Business card back">
    <div class="photo" role="img" aria-label="Beauty portrait of a model in lilac makeup holding a large pale purple flower"></div>
    <div class="brand"><span class="brand__dot"></span>LK Makeup Artistry</div>
  </section>

</main>
</body>
</html>
```